Book Cover Design Book About Commercial Real Estate Investing

I need a book cover designed for my upcoming book.
Need cover for paperback and hardcover book.

The Book is about investing in net lease commercial property.

The book title:

The Ground Rent Handbook
Proven Methods For KVR Asset Buyers
By Lou Barrow

Should be minimalist, clean, authoritative, convey money, trust, & growth
I think I like the colors white red and black.
I want a front cover at this time.

Samples I like are included. - the red white and blacks are my favorites

My company is The KVR Circle
you can learn more about Triple Net Properties at my website
www.TheKVRCircle.com

the symbol NNN = Triple net in commercial real estate

Target Market(s)

Affluent male conservative investors

Industry/Entity Type

Real Estate

Requirements
Nice to have
• Sports Motif - - diagrams of sports plays from playbook
• google - Diagrams of sports plays -

```html
<!DOCTYPE html>
<html lang="en">
<head>
<meta charset="utf-8">
<title>The KVR Ground Rent Handbook — Cover</title>
<link href="https://fonts.googleapis.com/css2?family=Arimo:wght@700&family=Tinos:wght@700&display=swap" rel="stylesheet">
<style>
  :root {
    --paper: #ffffff;
    --crimson: #b00000;
    --signal-red: #e0140f;
    --blush: #f6a6e2;
    --ink: #0a0a0a;
  }
  html, body {
    margin: 0;
    padding: 0;
    overflow: hidden;
    background: var(--paper);
  }
  .cover {
    position: relative;
    width: 1094px;
    height: 1200px;
    background: var(--paper);
    overflow: hidden;
  }
  .band { position: absolute; top: 0; height: 100%; }
  .band--spine-edge { left: 178px; width: 55px; background: var(--crimson); }
  .band--accent { left: 233px; width: 21px; background: var(--blush); }
  .band--right-edge { left: 1034px; width: 60px; background: var(--crimson); }

  /* Spine */
  .spine-title {
    position: absolute;
    left: 58px;
    top: 140px;
    margin: 0;
    writing-mode: vertical-rl;
    font-family: "Tinos", serif;
    font-weight: 700;
    line-height: 1.15;
    white-space: nowrap;
  }
  .spine-title__lead {
    display: block;
    color: var(--signal-red);
    font-size: 40px;
  }
  .spine-title__rest {
    display: block;
    color: var(--ink);
    font-size: 24px;
  }
  .spine-author {
    position: absolute;
    left: 86px;
    top: 810px;
    margin: 0;
    writing-mode: vertical-rl;
    font-family: "Tinos", serif;
    font-weight: 700;
    font-size: 33px;
    letter-spacing: 1px;
    color: var(--ink);
    white-space: nowrap;
  }

  /* Front */
  .front-title {
    position: absolute;
    left: 254px;
    width: 780px;
    top: 420px;
    margin: 0;
    text-align: center;
    font-family: "Tinos", serif;
    font-weight: 700;
    line-height: 1.1;
  }
  .front-title__lead {
    display: block;
    font-size: 104px;
    color: var(--signal-red);
  }
  .front-title__rest {
    display: block;
    font-size: 54px;
    color: var(--ink);
  }
  .subtitle {
    position: absolute;
    left: 254px;
    width: 780px;
    top: 862px;
    margin: 0;
    text-align: center;
    font-family: "Arimo", sans-serif;
    font-weight: 700;
    font-size: 28px;
    color: var(--ink);
  }
  .byline {
    position: absolute;
    left: 254px;
    width: 780px;
    top: 912px;
    margin: 0;
    text-align: center;
    font-family: "Tinos", serif;
    font-weight: 700;
    font-size: 28px;
    color: var(--signal-red);
  }
</style>
</head>
<body>
  <main class="cover">
    <div class="band band--spine-edge"></div>
    <div class="band band--accent"></div>
    <div class="band band--right-edge"></div>

    <p class="spine-title">
      <span class="spine-title__lead">The KVR</span>
      <span class="spine-title__rest">Ground Rent Handbook</span>
    </p>
    <p class="spine-author">LOU BARROW</p>

    <h1 class="front-title">
      <span class="front-title__lead">The KVR</span>
      <span class="front-title__rest">Ground Rent Handbook</span>
    </h1>
    <p class="subtitle">Proven Methods For KVR Asset Buyers</p>
    <p class="byline">By Lou Barrow</p>
  </main>
</body>
</html>
```